Vegan Jerky company needs a label for it's pouch, and a new logo

Dear Designers - this used to be a guaranteed project, however, due to the low quality of designs I have received, I have removed the guaranteed status. However, we need this product made and we will pay for a great, high quality design that meets the requirements of our brief.

We need sticker labels that will go onto the front and back of our vegan jerky package. Our package is a zip-sealable pouch, and we will either go with black, white or brown for the color of the pouch.

We need the concept, artwork, theme and logo designed. Pls choose the colors.

There will be four flavors. These can be finished as part of another project. The flavors are: Smoked Maple, Cracked Pepper, Teriyaki Sriracha, Original.

We are Lonny and Marva's Vegan Jerky.

Our food is vegan, non GMO, straight from the farm, organic, healthy, pure, clean, made in small batches and earth friendly. We use no chemicals or artificial flavors and our product is 100% natural.

Our kitchen is yours.
Updates

Low designer entries

Target Market(s)

Vegetarians, vegans, health conscious, ecological, intelligent, caring.

Industry/Entity Type

Food Production

Logo Text

"Lonny and Marva" and "Our Kitchen is Yours"

Colors

Designer to choose colors to be used in the design.

Requirements
Must have
• earth friendly design, classy, hipster, vegan design, shabby chic,
Nice to have
• i have no ideas really...
• We prefer black and while, with a little splash of color. The last file is an idea I had but please use your own vision.

```html
<!DOCTYPE html>
<html lang="en">
<head>
<meta charset="utf-8">
<title>Lonny and Marva's Vegan Jerky – Pouch Label</title>
<link rel="stylesheet" href="https://fonts.googleapis.com/css2?family=Cinzel:wght@400;700&display=swap">
<style>
  :root {
    --page-bg: #ffffff;
    --pouch-bg: #ececec;
    --pouch-edge: #d4d4d4;
    --label-line: #d9d9d9;
    --brand-maroon: #3f0b0b;
    --accent-red: #8e1414;
  }
  * { margin: 0; padding: 0; box-sizing: border-box; }
  html, body {
    width: 1200px;
    height: 1200px;
    overflow: hidden;
    background: var(--page-bg);
  }
  .canvas {
    position: relative;
    width: 1200px;
    height: 1200px;
  }
  .pouch-face {
    position: absolute;
    left: 280px;
    top: 60px;
    width: 640px;
    height: 1080px;
    background: var(--pouch-bg);
    border: 2px solid var(--pouch-edge);
    font-family: "Cinzel", Georgia, serif;
    text-align: center;
  }
  .label-frame {
    position: absolute;
    left: 96px;
    top: 238px;
    width: 448px;
    height: 786px;
    border: 1px solid var(--label-line);
  }
  .brand-block {
    position: absolute;
    top: 268px;
    left: 0;
    width: 100%;
  }
  .brand-dot {
    display: block;
    width: 44px;
    height: 44px;
    margin: 0 auto 18px;
    border-radius: 50%;
    background: var(--brand-maroon);
  }
  .brand-name {
    font-weight: 700;
    font-size: 58px;
    line-height: 1.1;
    letter-spacing: 1px;
    color: var(--brand-maroon);
  }
  .product-title {
    position: absolute;
    top: 618px;
    left: 0;
    width: 100%;
    color: var(--accent-red);
    font-weight: 400;
    line-height: 1;
  }
  .product-title .main {
    display: block;
    font-size: 112px;
  }
  .product-title .sub {
    display: block;
    margin-top: 6px;
    font-size: 72px;
    letter-spacing: 6px;
  }
  .natural-claim {
    position: absolute;
    top: 948px;
    left: 0;
    width: 100%;
    color: var(--accent-red);
    line-height: 1;
  }
  .natural-claim .figure {
    display: block;
    font-size: 40px;
  }
  .natural-claim .word {
    display: block;
    font-size: 20px;
    letter-spacing: 3px;
    margin-top: 0;
  }
</style>
</head>
<body>
  <main class="canvas">
    <section class="pouch-face">
      <div class="label-frame"></div>
      <div class="brand-block">
        <span class="brand-dot"></span>
        <div class="brand-name">Lonny and<br>Marva's</div>
      </div>
      <h1 class="product-title">
        <span class="main">VEGAN</span>
        <span class="sub">JERKY</span>
      </h1>
      <p class="natural-claim">
        <span class="figure">100%</span>
        <span class="word">NATURAL</span>
      </p>
    </section>
  </main>
</body>
</html>
```